Banner Ad for Premium Supplement - RIVERS BLOOM

We need banner ads designed for our premium supplement, Rivers Bloom.

Sizes to make (6): 125x125, 300x250, 240x400, 250x250, 160x600, 468x60

We sell mostly online via long form sales page. Here’s the link to our sales page:

https://store.vernalgoods.example/tidalfoodblend

On that page you will see the product itself and some of our styling.

Our main website is here: http://www.vernalgoods.example/

Our style is best described as a harmony between science and nature:

Science = high tech, sophisticated, polished, professional, premium, clean, trustworthy

Nature = healthy, wholesome, nutritious, organic, full of life

Attached to this project is an RTF file with the verbiage for our ads. There are 2 versions. Please make 1 design for each size, in both versions (total of 12 designs).

```html
<!DOCTYPE html>
<html lang="en">
<head>
<meta charset="utf-8">
<title>Rivers Bloom – Banner Set</title>
<link href="https://fonts.googleapis.com/css2?family=Lilita+One&family=Ubuntu:wght@400;500;700&display=swap" rel="stylesheet">
<style>
  :root{
    --page:#eceef0;
    --navy-top:#0a3570;
    --navy-bottom:#1d5fab;
    --sky-light:#c9f3ff;
    --sky-mid:#7fd9f5;
    --sky-deep:#2bb0e6;
    --teal-ink:#0f6d93;
    --violet-a:#5b1fa0;
    --violet-b:#8a2fc4;
    --lime:#d6f73c;
    --body-ink:#10263a;
    --btn-top:#ffd23a;
    --btn-bottom:#f29300;
    --btn-ink:#3b2a05;
    --bottle-dark:#2a1a0c;
    --bottle-green:#2f8f3a;
  }
  *{box-sizing:border-box;margin:0;padding:0}
  html,body{width:1200px;height:798px;overflow:hidden}
  body{
    background:var(--page);
    position:relative;
    font-family:"Ubuntu",sans-serif;
  }
  .banner{
    position:absolute;
    overflow:hidden;
    background:linear-gradient(180deg,var(--sky-light),var(--sky-mid) 55%,var(--sky-deep));
    box-shadow:0 1px 4px rgba(0,0,0,.25);
  }
  .banner > *{position:absolute}
  .tagline{
    left:0;right:0;top:0;
    background:linear-gradient(180deg,var(--navy-top),var(--navy-bottom));
    color:#fff;
    font-weight:500;
    text-align:center;
    display:flex;flex-direction:column;justify-content:center;
    white-space:nowrap;
  }
  .question{
    left:0;right:0;
    background:linear-gradient(180deg,#e6fbff,var(--sky-mid));
    color:var(--teal-ink);
    font-family:"Lilita One",sans-serif;
    text-align:center;
    display:flex;flex-direction:column;justify-content:center;
    line-height:1;
    letter-spacing:.5px;
    white-space:nowrap;
  }
  .claim{
    left:0;right:0;
    background:linear-gradient(90deg,var(--violet-a),var(--violet-b));
    color:var(--lime);
    font-weight:500;
    line-height:1;
    display:flex;flex-direction:column;justify-content:center;
    white-space:nowrap;
  }
  .claim strong{font-weight:700}
  .pitch{color:var(--body-ink);white-space:nowrap}
  .product-shot{
    background:
      radial-gradient(ellipse 30% 45% at 50% 62%,var(--bottle-green),transparent 70%),
      linear-gradient(180deg,transparent 4%,var(--bottle-dark) 18%,#3a2612 82%,transparent 98%);
    border-radius:6px;
  }
  .cta{
    background:linear-gradient(180deg,var(--btn-top),var(--btn-bottom));
    border-radius:20px;
    color:var(--btn-ink);
    font-family:"Lilita One",sans-serif;
    display:flex;align-items:center;justify-content:center;gap:6px;
    box-shadow:inset 0 1px 0 rgba(255,255,255,.6),0 1px 2px rgba(0,0,0,.3);
    white-space:nowrap;
  }
  .cta svg{flex:none}

  /* 160x600 */
  .sky{left:36px;top:17px;width:204px;height:763px}
  .sky .tagline{height:155px;font-size:37px;line-height:1.2}
  .sky .question{top:155px;height:81px;font-size:37px}
  .sky .claim{top:236px;height:94px;font-size:24px;line-height:1.1;text-align:center}
  .sky .pitch{top:340px;left:0;right:0;font-size:17px;line-height:1.28;text-align:center}
  .sky .product-shot{left:40px;top:478px;width:130px;height:236px}
  .sky .cta{left:6px;top:726px;width:191px;height:34px;font-size:20px}

  /* 468x60 */
  .board{left:265px;top:17px;width:597px;height:77px}
  .board .tagline{width:105px;right:auto;height:77px;font-size:17px;line-height:1.12;text-align:left;padding-left:8px}
  .board .question{left:105px;right:auto;top:0;width:146px;height:77px;font-size:24px}
  .board .claim{left:251px;right:auto;top:0;width:204px;height:77px;font-size:20px;line-height:1.05;text-align:center}
  .board .product-shot{left:500px;top:0;width:64px;height:42px}
  .board .cta{left:466px;top:48px;width:123px;height:22px;font-size:14px}

  /* 240x400 */
  .tower{left:265px;top:119px;width:306px;height:510px}
  .tower .tagline{height:36px;font-size:23px}
  .tower .question{top:36px;height:50px;font-size:29px}
  .tower .claim{top:86px;height:140px;font-size:38px;line-height:1.08;padding-left:10px}
  .tower .pitch{top:234px;left:8px;font-size:17.5px;line-height:1.3}
  .tower .product-shot{left:168px;top:245px;width:136px;height:232px}
  .tower .cta{left:6px;top:471px;width:172px;height:33px;font-size:18px}

  /* 300x250 */
  .rect{left:597px;top:119px;width:383px;height:319px}
  .rect .tagline{height:32px;font-size:22px}
  .rect .question{top:32px;height:53px;font-size:36px;text-align:left;padding-left:14px}
  .rect .claim{top:85px;height:87px;font-size:25px;padding-left:18px}
  .rect .pitch{top:180px;left:18px;font-size:15px;line-height:1.25}
  .rect .product-shot{left:240px;top:88px;width:138px;height:224px}
  .rect .cta{left:32px;top:280px;width:172px;height:28px;font-size:17px}

  /* 250x250 */
  .square{left:597px;top:463px;width:319px;height:319px}
  .square .tagline{height:34px;font-size:21px}
  .square .question{top:34px;height:45px;font-size:30px;text-align:left;padding-left:8px}
  .square .claim{top:79px;height:89px;font-size:24px;padding-left:8px}
  .square .pitch{top:176px;left:8px;font-size:14.5px;line-height:1.25}
  .square .product-shot{left:210px;top:86px;width:106px;height:228px}
  .square .cta{left:19px;top:281px;width:172px;height:29px;font-size:17px}

  /* 125x125 */
  .tile{left:1005px;top:119px;width:159px;height:159px}
  .tile .tagline{height:15px;font-size:10px}
  .tile .question{top:15px;height:26px;font-size:15px;text-align:left;padding-left:4px}
  .tile .claim{top:41px;height:82px;font-size:10.5px;line-height:1.12;padding-left:4px}
  .tile .product-shot{left:106px;top:41px;width:52px;height:86px}
  .tile .cta{left:4px;top:132px;width:132px;height:22px;font-size:12px}
</style>
</head>
<body>

<section class="banner sky" aria-label="Skyscraper banner 160 by 600">
  <div class="tagline"><span>- ENERGY -</span><span>- FOCUS -</span><span>- YOUTH -</span></div>
  <div class="question"><span>DID YOU</span><span>KNOW...</span></div>
  <p class="claim"><span>100% of Life on<br>Earth relies on<br><strong>ONE</strong> Superfood?</span></p>
  <p class="pitch">See why &amp; how<br>this little known<br>substance triggers<br>your body to create<br>TRILLIONS of healthy<br>new cells!</p>
  <div class="product-shot" role="img" aria-label="Three Rivers Bloom dropper bottles"></div>
  <a class="cta">CLICK HERE <svg width="12" height="12" viewBox="0 0 12 12"><circle cx="6" cy="6" r="6" fill="#e07800"/><path d="M4.5 3 L8.5 6 L4.5 9Z" fill="#fff"/></svg></a>
</section>

<section class="banner board" aria-label="Leaderboard banner 468 by 60">
  <div class="tagline"><span>- ENERGY</span><span>- FOCUS</span><span>- YOUTH</span></div>
  <div class="question"><span>DID YOU</span><span>KNOW...</span></div>
  <p class="claim"><span>100% of Life on<br>Earth relies on<br><strong>ONE</strong> Superfood?</span></p>
  <div class="product-shot" role="img" aria-label="Three Rivers Bloom dropper bottles"></div>
  <a class="cta">CLICK HERE <svg width="10" height="10" viewBox="0 0 12 12"><circle cx="6" cy="6" r="6" fill="#e07800"/><path d="M4.5 3 L8.5 6 L4.5 9Z" fill="#fff"/></svg></a>
</section>

<section class="banner tower" aria-label="Banner 240 by 400">
  <div class="tagline"><span>ENERGY - FOCUS - YOUTH</span></div>
  <div class="question"><span>DID YOU KNOW...</span></div>
  <p class="claim"><span>100% of Life on<br>Earth relies on<br><strong>ONE</strong> Superfood?</span></p>
  <p class="pitch">See why &amp; how<br>this little known<br>substance triggers<br>your body to create<br>TRILLIONS<br>of healthy<br>new cells!</p>
  <svg style="left:52px;top:420px" width="42" height="30" viewBox="0 0 42 30"><path d="M2 2 Q10 22 36 24" fill="none" stroke="#1b3550" stroke-width="1.5"/><path d="M30 19 L37 24 L30 28" fill="none" stroke="#1b3550" stroke-width="1.5"/></svg>
  <div class="product-shot" role="img" aria-label="Three Rivers Bloom dropper bottles"></div>
  <a class="cta">CLICK HERE <svg width="12" height="12" viewBox="0 0 12 12"><circle cx="6" cy="6" r="6" fill="#e07800"/><path d="M4.5 3 L8.5 6 L4.5 9Z" fill="#fff"/></svg></a>
</section>

<section class="banner rect" aria-label="Medium rectangle banner 300 by 250">
  <div class="tagline"><span>ENERGY - FOCUS - YOUTH</span></div>
  <div class="question"><span>DID YOU KNOW...</span></div>
  <p class="claim"><span>100% of Life on<br>Earth relies on<br><strong>ONE</strong> Superfood?</span></p>
  <p class="pitch">See why &amp; how this little<br>known substance triggers<br>your body to create<br>TRILLIONS of healthy<br>new cells!</p>
  <div class="product-shot" role="img" aria-label="Three Rivers Bloom dropper bottles"></div>
  <a class="cta">CLICK HERE <svg width="12" height="12" viewBox="0 0 12 12"><circle cx="6" cy="6" r="6" fill="#e07800"/><path d="M4.5 3 L8.5 6 L4.5 9Z" fill="#fff"/></svg></a>
</section>

<section class="banner square" aria-label="Square banner 250 by 250">
  <div class="tagline"><span>ENERGY - FOCUS - YOUTH</span></div>
  <div class="question"><span>DID YOU KNOW...</span></div>
  <p class="claim"><span>100% of Life on<br>Earth relies on<br><strong>ONE</strong> Superfood?</span></p>
  <p class="pitch">See why &amp; how this little<br>known substance triggers<br>your body to create<br>TRILLIONS of healthy<br>new cells!</p>
  <div class="product-shot" role="img" aria-label="Three Rivers Bloom dropper bottles"></div>
  <a class="cta">CLICK HERE <svg width="12" height="12" viewBox="0 0 12 12"><circle cx="6" cy="6" r="6" fill="#e07800"/><path d="M4.5 3 L8.5 6 L4.5 9Z" fill="#fff"/></svg></a>
</section>

<section class="banner tile" aria-label="Button banner 125 by 125">
  <div class="tagline"><span>ENERGY - FOCUS - YOUTH</span></div>
  <div class="question"><span>DID YOU KNOW...</span></div>
  <p class="claim"><span>100% OF LIFE<br>ON EARTH<br>RELIES ON<br><strong>ONE</strong><br>SUPERFOOD?</span></p>
  <div class="product-shot" role="img" aria-label="Three Rivers Bloom dropper bottles"></div>
  <a class="cta">CLICK HERE <svg width="9" height="9" viewBox="0 0 12 12"><circle cx="6" cy="6" r="6" fill="#e07800"/><path d="M4.5 3 L8.5 6 L4.5 9Z" fill="#fff"/></svg></a>
</section>

</body>
</html>
```